Improve My Resume Design to be easier for the reader and the recruiter

I need to improve my resume design to make it easier to read and attract employer eyes in a very professional way. And the graphs should be neat, nice and professional. - You can use the below logos as the companies that I worked with are so famous.

Detailed information about me is inside the CV.

Target Market(s)

Big Companies and Famous recruiters

Industry/Entity Type

Government

Colors

Designer to choose colors to be used in the design.

Requirements
Must have
• Infographics .. Easy to Read.
Nice to have
• Charts, infographics.
Should not have
• not professional colours.

```html
<!DOCTYPE html>
<html lang="en">
<head>
<meta charset="utf-8">
<title>Resume – Experience and Developments</title>
<link href="https://fonts.googleapis.com/css2?family=Open+Sans:wght@400;600;700;800&display=swap" rel="stylesheet">
<style>
:root{
  --navy:#1f2d3d;
  --blue:#1f6fb5;
  --ink:#222;
  --muted:#555;
  --rule:#d3d6da;
  --paper:#fff;
  --accent:#c0392b;
}
*{margin:0;padding:0;box-sizing:border-box}
html,body{width:853px;height:1200px;overflow:hidden;background:var(--paper)}
body{font-family:"Open Sans",Arial,sans-serif;color:var(--ink);position:relative}
.timeline{position:absolute;left:362px;top:0;width:2px;height:870px;background:var(--rule)}
.bullets{list-style:none;font-size:11.5px;line-height:1.5}
.bullets li{position:relative;padding-left:16px;margin-bottom:3px}
.bullets li::before{content:"";position:absolute;left:2px;top:7px;width:5px;height:5px;border-radius:50%;background:var(--navy)}
.prev-duties{position:absolute;left:378px;top:14px;width:440px}
.job-date{position:absolute;left:185px;top:334px;font-weight:700;font-size:14px;color:var(--navy)}
.employer{position:absolute;left:186px;top:368px;display:flex;align-items:center;gap:8px;font-size:12px;font-weight:700;color:var(--accent)}
.employer .mark{width:14px;height:14px;background:var(--accent)}
.job-title{position:absolute;left:384px;top:332px;font-size:17px;font-weight:700;color:var(--navy)}
.resp-band{position:absolute;left:378px;top:364px;width:447px;height:26px;background:var(--blue);color:#fff;font-weight:700;font-size:14px;padding:3px 12px}
.duties{position:absolute;left:378px;top:402px;width:440px}
.duties li::before{border-radius:0}
.dev-band{position:absolute;left:0;top:906px;width:853px;height:56px;background:var(--navy);display:flex;align-items:center;padding-left:20px;gap:16px}
.dev-band h2{color:#fff;font-size:27px;font-weight:800;letter-spacing:.5px}
.gear{width:36px;height:36px}
.dev-list{position:absolute;left:85px;top:984px;width:730px;list-style:none;font-size:12.5px;font-weight:700;line-height:1.5}
.dev-list li{position:relative;padding-left:20px;margin-bottom:4px}
.dev-list li::before{content:"";position:absolute;left:0;top:6px;width:8px;height:8px;background:var(--blue)}
</style>
</head>
<body>
<div class="timeline"></div>

<ul class="bullets prev-duties">
  <li>Ensure that business requirements are effectively translated into detailed functional and technical specifications from which appropriate business systems can be implemented or existing systems enhanced.</li>
  <li>Planned future phases of e-Government initiatives related to new service and delivery channels.</li>
  <li>Collaborated with Development and e-Government Sections for IT projects and liaised with external software vendors and IT consultants for outsourced projects.</li>
  <li>Reviewed Project Overview Statement POS, identified project priority with Portfolio Management and scheduled project implementation with PMO.</li>
  <li>Set up and ensured communication among organisation systems and applications.</li>
</ul>

<div class="job-date">(Jul 2007 - Jul 2008)</div>
<div class="employer"><span class="mark"></span>Harbor City Council</div>
<div class="job-title">Business Support Engineer</div>
<div class="resp-band">Responsibilities:</div>

<ul class="bullets duties">
  <li>Rendered technical support for 170 online Services, generated reports and ensured prompt resolution of user issues.</li>
  <li>Researched, diagnosed, troubleshot and identified solutions to resolve system/service related technical issues.</li>
  <li>Enhanced customer satisfaction by providing quality service and resolving critical/escalated technical issues on time.</li>
  <li>Conducted training sessions for internal users to train them on new e-services deployed in the organisation.</li>
  <li>Liaised with vendors with regards to the upcoming new projects in the Support Unit.</li>
  <li>Efficiently handled online transformation project of the e-Government Section.</li>
  <li>Maintained detailed reports listing requests to technical assistance, steps taken to resolve them, and the specific individuals involved.</li>
</ul>

<div class="dev-band">
  <svg class="gear" viewBox="0 0 36 36" aria-hidden="true">
    <circle cx="18" cy="18" r="17" fill="#fff"/>
    <g fill="var(--navy)">
      <circle cx="18" cy="18" r="7"/>
      <rect x="16" y="7" width="4" height="22"/>
      <rect x="7" y="16" width="22" height="4"/>
      <rect x="16" y="7" width="4" height="22" transform="rotate(45 18 18)"/>
      <rect x="16" y="7" width="4" height="22" transform="rotate(-45 18 18)"/>
    </g>
    <circle cx="18" cy="18" r="3" fill="#fff"/>
  </svg>
  <h2>DEVELOPMENTS</h2>
</div>

<ul class="dev-list">
  <li>Northwind Certified Professional in Developing WebForge Web Applications Using Studio Suite</li>
  <li>Certified Business Process Specialist (CBPS) Certificate</li>
  <li>Northwind PPM 2010 Portfolio Management and Business Analysis Training</li>
  <li>Meridian 8.0 Essentials Ed1 Certificate from Corvanta Academy (20 Sep 2011 Until 28th Sep 2011)</li>
  <li>Corvanta Course</li>
  <li>IT - Web Development Training</li>
  <li>Introduction to Visual Script Programming</li>
  <li>Many Oil &amp; Gas Conferences and Seminars in Malaysia and Iraq</li>
</ul>
</body>
</html>
```